Sleek modern site for stage hypnotist who does high school, college, university and corporate gigs.

Need a website design for stage hypnotist Mark Dolloway
I'm using a plinkio domain

Mark Dolloway is a stage hypnotist who does high school shows , colleges, corporate and fundraisers
Looking for something sleek and modern looking.
I need about 4 pages at least one main describing what i do
1st page Describes what events i do (high school, college, corporate, weddings, fundraisers, fairs)
2nd page would be an about/bio page
3rd FAQ page about hypnosis.

*what venues do you work with?
*how long is your show?
*How do we promote the show?
*is it safe
*are you insured?
*how much does it cost?
4th page will be a contact page and link to my social media like Snapvue, chirpnet, and possibly Friendlyn.

Included is a few pictures that I'll probably including on the site. I'm waiting on the rest for photoshoot at the this week. Some of these pictures probably will have different stock backgrounds other than grey (something like a las vegas strip or a stage.

Visually I'm looking for a cool color scheme.

Target Market(s)

High school for now but college and corporate down the road.

Industry/Entity Type

Entertainment Industry

Coding

Coded - Design and coding required

Number of Pages Required

4 page

Font styles to use
Serif
Sans Serif

Colors
3277b5
85acd3
9d9d9d
5c5c5c
cbcbcb
aaaaaa
1b1b1b
333333

Requirements
Must have
• MUST BE ABLE TO WORK WITH PLINKIO
• A sleek and professional look as if I've been doing this for years.
• The ability to edit the text of the site so i can improve upon the persuasive parts if need be.
• I also will be getting more promotional photos in the 5 or 6 days after the deadline days so if i pick your project i'd like to be able to integrate some of them into the design. The 3 photos i provided are somewhat place holders to give you an idea of the rest that are to come.
Nice to have
• drop down links
Should not have
• if you zoobit other stage hypnotists their sites are a bit stale and not that modern.

```html
<!DOCTYPE html>
<html lang="en">
<head>
<meta charset="utf-8">
<title>Mark Dolloway — Stage Hypnotist</title>
<link href="https://fonts.googleapis.com/css2?family=Poppins:ital,wght@0,400;0,500;0,600;0,700;0,800;1,400&family=Great+Vibes&display=swap" rel="stylesheet">
<style>
:root{
  --ink:#1b1b1b;
  --charcoal:#222222;
  --graphite:#333333;
  --mid:#5c5c5c;
  --soft:#9d9d9d;
  --pale:#cbcbcb;
  --white:#ffffff;
  --tan:#b8875a;
  --text-dark:#2a2a2a;
}
*{margin:0;padding:0;box-sizing:border-box}
html,body{width:1200px;height:3061px;overflow:hidden}
body{font-family:'Poppins',sans-serif;background:var(--white);position:relative;color:var(--white)}
section,footer{position:absolute;left:0;width:1200px}

/* hero */
.hero{top:0;height:650px;overflow:hidden;background:var(--ink)}
.hero-backdrop{position:absolute;inset:0;background:radial-gradient(circle at 760px 420px,#2e2e2e 0,#1c1c1c 45%,#111111 85%)}
.hero-photo{position:absolute;left:600px;top:0;width:400px;height:650px;background:linear-gradient(180deg,#3a3a3d 0%,#1d1d22 55%,#141418 100%)}
.menu-btn{position:absolute;left:1062px;top:37px;width:40px;height:40px;border-radius:50%;background:#6a6a6a;display:flex;flex-direction:column;justify-content:center;align-items:center;gap:4px}
.menu-btn span{display:block;width:16px;height:2px;background:var(--white)}
.hero-title{position:absolute;left:98px;top:228px;font-size:44px;font-weight:700;letter-spacing:1px;line-height:60px}
.hero-text{position:absolute;left:98px;top:300px;width:410px;font-size:12.5px;line-height:27px;color:#e6e6e6}
.btn-outline{position:absolute;left:98px;top:406px;width:118px;height:38px;border:2px solid var(--white);font-size:13px;font-weight:500;display:flex;align-items:center;justify-content:center}

/* about */
.about{top:650px;height:1120px;background:var(--charcoal)}
.services-cut{position:absolute;left:0;top:0}
.section-title{position:absolute;left:0;width:100%;text-align:center;font-weight:600}
.about .section-title{top:56px;font-size:38px}
.divider{position:absolute;left:599px;width:2px;background:var(--pale)}
.divider::after{content:"";position:absolute;left:-5px;top:50%;width:12px;height:12px;margin-top:-6px;border-radius:50%;background:var(--white)}
.about .divider{top:132px;height:86px}
.about-text{position:absolute;left:160px;top:236px;width:880px;text-align:center;font-size:13px;line-height:30px;color:#e0e0e0}
.signature{position:absolute;left:0;width:100%;text-align:center;font-family:'Great Vibes',cursive;color:var(--white)}
.about .signature{top:420px;font-size:42px}

/* what I do */
.ghost-word{position:absolute;left:135px;top:583px;font-size:48px;font-weight:800;color:#3a3a3a;letter-spacing:1px;line-height:60px}
.services-title{position:absolute;left:135px;top:628px;font-size:48px;font-weight:600;line-height:60px}
.services-mark{position:absolute;left:101px;top:614px;width:2px;height:82px;background:var(--pale)}
.services-mark::after{content:"";position:absolute;left:-5px;top:36px;width:12px;height:12px;border-radius:50%;background:var(--white)}
.services-text{position:absolute;left:98px;top:730px;width:360px;font-size:13px;line-height:29px;color:#e0e0e0}
.services-list{position:absolute;left:98px;top:840px;list-style:none;font-size:13px;line-height:29.5px;color:#e0e0e0}
.tile{position:absolute;width:294px;height:245px;background:linear-gradient(160deg,#c99a6b 0%,#ad7f55 100%);display:flex;flex-direction:column;align-items:center;justify-content:center;gap:10px}
.tile-label{font-size:22px;font-weight:600;color:var(--white)}
.tile svg{width:52px;height:52px}
.tile-1{left:496px;top:595px}
.tile-2{left:806px;top:595px}
.tile-3{left:496px;top:860px}
.tile-4{left:806px;top:860px}
.bottom-divider{position:absolute;left:599px;top:1110px;width:2px;height:77px;background:var(--graphite)}
.bottom-divider::after{content:"";position:absolute;left:-5px;top:71px;width:12px;height:12px;border-radius:50%;background:var(--graphite)}

/* testimonials */
.testimonials{top:1770px;height:608px;color:var(--text-dark)}
.testimonials .section-title{top:160px;font-size:40px;font-weight:500}
.avatar{position:absolute;left:529px;top:251px;width:142px;height:142px;border-radius:50%;border:5px solid #dcdcdc;background:radial-gradient(circle at 50% 40%,#6d7a8c 0%,#2c3444 70%)}
.quote-mark{position:absolute;font-family:Georgia,serif;font-size:100px;font-weight:700;line-height:1;color:var(--text-dark)}
.quote-open{left:180px;top:354px}
.quote-close{left:970px;top:468px}
.testimonial-text{position:absolute;left:170px;top:420px;width:860px;text-align:center;font-size:12.5px;font-style:italic;line-height:28px;color:#444}
.testimonial-author{position:absolute;left:0;width:100%;top:518px;text-align:center;font-size:15px;font-style:italic;color:#444}
.testimonial-author b{font-weight:600;color:var(--text-dark)}

/* newsletter */
.newsletter{top:2378px;height:473px;background:linear-gradient(180deg,#4a4440 0%,#2d2926 55%,#3a302a 100%)}
.newsletter .signature{top:128px;font-size:44px}
.newsletter-title{position:absolute;left:0;width:100%;top:200px;text-align:center;font-size:29px;font-weight:600;letter-spacing:.5px}
.subscribe{position:absolute;left:351px;top:271px;width:498px;height:41px;display:flex;border-radius:21px;overflow:hidden}
.subscribe-input{flex:1;background:var(--white);color:#888;font-size:12px;display:flex;align-items:center;padding-left:24px}
.subscribe-btn{width:125px;background:var(--tan);font-size:12px;display:flex;align-items:center;justify-content:center}

/* footer */
.site-footer{top:2851px;height:210px;background:var(--charcoal)}
.footer-nav{position:absolute;left:0;width:100%;top:44px;text-align:center;font-size:13px;font-weight:500;letter-spacing:.5px}
.footer-nav span.sep{margin:0 20px}
.copyright{position:absolute;left:0;width:100%;top:88px;text-align:center;font-size:13px;color:#e0e0e0}
.social{position:absolute;left:0;width:100%;top:138px;display:flex;justify-content:center;gap:8px}
.social span{width:29px;height:29px;border-radius:50%;background:var(--white)}
</style>
</head>
<body>

<section class="hero">
  <div class="hero-backdrop" role="img" aria-label="Dark hypnotic spiral backdrop"></div>
  <div class="hero-photo" role="img" aria-label="Portrait of Mark Dolloway reaching a hand toward the viewer"></div>
  <div class="menu-btn"><span></span><span></span><span></span></div>
  <h1 class="hero-title">MARK DOLLOWAY</h1>
  <p class="hero-text">Sed ut perspiciatis unde omnis iste natus error sit voluptatem accusantium doloremque laudantium, totam rem aperiam, eaque ipsa quae ab illo inventore</p>
  <div class="btn-outline">READ MORE</div>
</section>

<section class="about">
  <svg class="services-cut" width="1200" height="1120" aria-hidden="true">
    <polygon points="0,1115 1200,809 1200,1120 0,1120" fill="#ffffff"/>
  </svg>
  <h2 class="section-title">About Me</h2>
  <div class="divider"></div>
  <p class="about-text">Sed ut perspiciatis unde omnis iste natus error sit voluptatem accusantium doloremque laudantium, totam rem aperiam, eaque ipsa quae ab illo inventore veritatis et quasi architecto beatae vitae dicta sunt explicabo. Nemo enim ipsam voluptatem quia voluptas sit aspernatur aut odit aut fugit, sed quia consequuntur magni dolores eos qui ratione voluptatem sequi nesciunt. Neque porro quisquam est, qui dolorem ipsum quia dolor sit amet, consectetur, adipisci velit, sed quia non numquam eius modi tempora incidunt ut labore et dolore magnam aliquam quaerat voluptatem.</p>
  <div class="signature">Mark Dolloway</div>

  <div class="ghost-word">HYPNOTIST</div>
  <div class="services-mark"></div>
  <h2 class="services-title">WHAT I DO</h2>
  <p class="services-text">Sed ut perspiciatis unde omnis iste natus error sit voluptatem accusantium doloremque laudantium, totam rem aperiam, eaque ipsa quae</p>
  <ul class="services-list">
    <li>High School</li><li>College</li><li>Corporate</li><li>Weddings</li><li>Fundraisers</li><li>Fairs</li>
  </ul>

  <div class="tile tile-1" role="img" aria-label="Students gathered at a high school show">
    <svg viewBox="0 0 52 52" fill="none" stroke="#fff" stroke-width="2.5"><path d="M6 46h40M10 46V24h32v22M4 24l22-12 22 12M26 12V4h8v4h-8"/><rect x="22" y="34" width="8" height="12"/></svg>
    <span class="tile-label">High School</span>
  </div>
  <div class="tile tile-2" role="img" aria-label="Team of colleagues at a corporate event">
    <svg viewBox="0 0 52 52" fill="#fff"><circle cx="16" cy="14" r="7"/><circle cx="36" cy="14" r="7"/><path d="M4 46c0-12 5-20 12-20s12 8 12 20zM24 46c0-12 5-20 12-20s12 8 12 20z"/></svg>
    <span class="tile-label">Corporate</span>
  </div>
  <div class="tile tile-3" role="img" aria-label="Bride and groom at a wedding celebration">
    <svg viewBox="0 0 52 52" fill="none" stroke="#fff" stroke-width="2.5"><path d="M26 20c-4-8-16-6-14 2 1 6 14 14 14 14s13-8 14-14c2-8-10-10-14-2z"/><path d="M6 48h40"/></svg>
    <span class="tile-label">Weddings</span>
  </div>
  <div class="tile tile-4" role="img" aria-label="Ferris wheel at a county fair">
    <svg viewBox="0 0 52 52" fill="none" stroke="#fff" stroke-width="2.5"><circle cx="26" cy="22" r="16"/><path d="M26 6v32M10 22h32M15 11l22 22M37 11 15 33M26 22 16 48M26 22l10 26M12 48h28"/></svg>
    <span class="tile-label">Fairs</span>
  </div>
  <div class="bottom-divider"></div>
</section>

<section class="testimonials">
  <h2 class="section-title">Customer Testimonials</h2>
  <div class="avatar" role="img" aria-label="Portrait of the reviewing customer"></div>
  <div class="quote-mark quote-open">&ldquo;</div>
  <p class="testimonial-text">Lorem ipsum dolor sit amet, consectetur adipiscing elit, sed do eiusmod tempor incididunt ut labore et dolore magna aliqua. Ut enim ad minim veniam, quis nostrud exercitation ullamco laboris nisi ut aliquip ex ea commodo consequat. Duis aute irure dolor in reprehenderit in voluptate velit esse cillum dolore eu fugiat nulla pariatur. Excepteur sint occaecat</p>
  <p class="testimonial-author"><b>John Doe</b> - Nemo enim ipsam voluptatem</p>
  <div class="quote-mark quote-close">&rdquo;</div>
</section>

<section class="newsletter" role="img" aria-label="Row of hanging crystal pendulums in soft warm light">
  <div class="signature">Mark Dolloway</div>
  <h2 class="newsletter-title">SIGN UP FOR NEWSLETTER</h2>
  <div class="subscribe">
    <div class="subscribe-input">Enter your E - mail</div>
    <div class="subscribe-btn">SUBSCRIBE</div>
  </div>
</section>

<footer class="site-footer">
  <nav class="footer-nav">HOME<span class="sep">/</span>ABOUT<span class="sep">/</span>FAQ<span class="sep">/</span>CONTACT</nav>
  <p class="copyright">2018 © Copyrights Mark Dolloway.All Rights Reserved</p>
  <div class="social"><span></span><span></span><span></span><span></span><span></span></div>
</footer>

</body>
</html>
```